Corvana Power Holdings Website

We have color scheme, logo and content, but need a design options in PDF format for the website. The PDF should guide us in how to use the color scheme and fonts in the site design (what background colors to use where, what link and hover colors to you, when to use which fonts...)

Corvana Power Holdings wants a conservative and straightforward website design that is in line with the banking industry. At the same time, Corvana wants the design to be innovative and cutting-edge in line with the renewable energy industry. Overall, the site design must be present the company as professional, serious, knowledgeable, experienced, reliable, and successful as well as a global good citizen.
Updates

We are closing this project. Thank you all for your beautiful work. Our designer was sick, but informed us today that she is better and able to resume her work. So we are closing this project and restarting work with her. Wish you all health and success.

Target Market(s)

investors, partners, developers, investment community, private equity community

Industry/Entity Type

Investment

Number of Pages Required

2 page

Requirements
Must have
• The color scheme is attached.
The logo is attached.
Fonts are Questrial and Cormorant (as used in logo).
The site must use these colors and fonts and logo design.

The 2 pages we need designed are the homepage and the portfolio page.
Homepage - The portfolio map on the homepage will be an image like with hotspots that link to portfolio items. This map image might go well with logo:
https://www.pixdrovo.com/abstract-polygon-world-map-vector-illustration-geometric-structure-in-blue-color-for-presentation-booklet-website-and-other-design-projects-pol-image550392817.html
But we would need to zoom in on Israel and EU, and leave out US / Asia-Pacific.
The way the map will work technically (using hotspots) should be something like:
https://tarvimpower.co.il/geographic-spread/.
Portfolio Page - The portfolio map there will be a Google Map/
Nice to have
• The content for the site is attached as a Word Doc, and much of it is in place at http://corvanafund.com.node4821.hostmarvo.de/. The design must fit this content, but we are open to some layout changes.
Design Requests:
• nav bar – light animation like https://pelludovet.com/ and https://www.qz-relocationlaw.com/
• innovative, unique design with welcoming, appealing, modern feel
• engaging content display by using parallax and subtle movement
• clean, intuitive, easy to navigation layout

```html
<!DOCTYPE html>
<html lang="en">
<head>
<meta charset="utf-8">
<title>Corvana Power Holdings</title>
<link href="https://fonts.googleapis.com/css2?family=Questrial&family=Cormorant:wght@500&family=Roboto+Condensed:wght@700&family=Roboto:wght@400&display=swap" rel="stylesheet">
<style>
:root{
  --green:#52a462;
  --lime:#7dbb2e;
  --link:#5aaa63;
  --blue:#3a8fc0;
  --ink:#111;
  --grey-text:#6b6b6b;
  --panel-grey:#f2f2f2;
  --footer:#161a1a;
  --grad-left:#c1ea5a;
  --grad-right:#50b0ea;
}
*{margin:0;padding:0;box-sizing:border-box}
html,body{width:1200px;height:2467px;overflow:hidden}
body{font-family:'Questrial',sans-serif;color:var(--ink);background:#fff;position:relative}
a{color:inherit}

/* hero */
.hero{position:absolute;left:0;top:0;width:1200px;height:552px;
  background:linear-gradient(180deg,#1d2a4c 0%,#34405e 35%,#6b5a4c 70%,#3e3a3c 100%);}
.brand{position:absolute;left:177px;top:12px;display:flex;align-items:center;gap:10px;color:#fff;font-size:22px;letter-spacing:.5px}
.brand-dot{width:36px;height:36px;border-radius:50%;background:#fff}
.main-nav{position:absolute;left:763px;top:22px;display:flex;gap:13px;font-size:11px;color:#fff}
.main-nav .active{color:#7fc24a}
.hero-title{position:absolute;left:0;width:1200px;top:248px;text-align:center;font-size:41px;color:#fff;letter-spacing:-.5px;text-shadow:0 2px 6px rgba(0,0,0,.5)}
.hero-title span{color:var(--lime)}
.hero-sub{position:absolute;left:0;width:1200px;top:325px;text-align:center;font-size:23px;line-height:39px;color:#fff;text-shadow:0 2px 6px rgba(0,0,0,.5)}

/* stats */
.stats{position:absolute;top:552px;left:0;width:1200px;height:80px;background:#fff;border-bottom:1px solid #e6e6e6}
.stat{position:absolute;top:18px}
.stat-num{font-size:20px}
.stat-label{font-size:9px;color:#555;margin-top:4px}
.stat-div{position:absolute;top:0;width:1px;height:80px;background:#e4e4e4}

/* about / team */
.about{position:absolute;top:632px;left:0;width:747px;height:365px;background:var(--panel-grey)}
.team{position:absolute;top:632px;left:747px;width:453px;height:365px;background:var(--green);color:#fff}
.eyebrow{font-family:'Roboto Condensed',sans-serif;font-weight:700;font-size:10px;letter-spacing:.3px}
.about .eyebrow{position:absolute;left:176px;top:55px;color:#7d8590}
.team .eyebrow{position:absolute;left:43px;top:55px}
.panel-title{font-size:38px;line-height:41px;letter-spacing:1px}
.about .panel-title{position:absolute;left:175px;top:85px}
.about .panel-title span{color:var(--blue)}
.team .panel-title{position:absolute;left:43px;top:85px}
.panel-text{font-size:17px;line-height:24.5px}
.about .panel-text{position:absolute;left:176px;top:188px;width:270px;color:var(--grey-text)}
.team .panel-text{position:absolute;left:43px;top:188px;width:280px}
.more-link{font-size:12px;display:flex;align-items:center;gap:6px}
.about .more-link{position:absolute;left:178px;top:316px;color:var(--link)}
.team .more-link{position:absolute;left:43px;top:312px;color:#fff}
.accent-circle{position:absolute;left:646px;top:273px;width:74px;height:74px;border-radius:50%;background:var(--green)}
.turbine-photo{position:absolute;left:460px;top:46px;width:232px;height:279px;background:linear-gradient(180deg,#c9d3db 0%,#b9c2c2 45%,#6e8a5a 75%,#4f6b3e 100%)}

/* approach */
.approach{position:absolute;top:997px;left:0;width:1200px;height:343px;background:linear-gradient(90deg,var(--grad-left),#8fd59e 45%,var(--grad-right));color:#fff;text-align:center}
.approach-kicker{position:absolute;top:47px;width:100%;font-size:15px;letter-spacing:.3px}
.approach-title{position:absolute;top:87px;width:100%;font-size:30px;letter-spacing:.5px}
.approach-text{position:absolute;top:133px;left:330px;width:540px;font-family:'Roboto',sans-serif;font-size:16.5px;line-height:25.5px}
.btn-more{position:absolute;left:520px;top:254px;width:138px;height:41px;background:#fff;border-radius:3px;color:var(--link);font-size:14px;display:flex;align-items:center;justify-content:center;gap:8px}

/* portfolio */
.portfolio-intro{position:absolute;top:1390px;width:1200px;text-align:center;font-size:12.5px;line-height:22px}
.portfolio-note{position:absolute;top:1455px;width:1200px;text-align:center;font-size:12.5px;line-height:22px}
.portfolio-note a{color:var(--link);font-size:16px}
.map{position:absolute;left:182px;top:1571px;width:833px;height:541px;border-radius:40px;background:radial-gradient(ellipse at 50% 45%,#bdbdbd 0%,#9a9a9a 55%,#e6e6e6 100%)}
.map-tag{position:absolute;background:#000;color:#fff;font-size:14px;padding:1px 8px;line-height:18px}
.map-lines{position:absolute;left:0;top:0}

/* footer */
.site-footer{position:absolute;top:2180px;left:0;width:1200px;height:287px;background:var(--footer);color:#fff}
.footer-brand{position:absolute;top:42px;width:100%;display:flex;justify-content:center;align-items:center;gap:14px;font-size:38px}
.footer-dot{width:56px;height:56px;border-radius:50%;background:var(--lime)}
.footer-address{position:absolute;top:152px;width:100%;text-align:center;font-size:14px}
.footer-contacts{position:absolute;top:178px;left:292px;width:620px;display:flex;justify-content:space-between;font-size:14px;color:#ddd}
.footer-contacts b{font-weight:400;color:#fff;font-family:'Roboto Condensed',sans-serif;font-weight:700}
.footer-credit{position:absolute;top:222px;left:289px;font-size:14px;color:var(--link)}
.footer-copy{position:absolute;top:218px;left:666px;font-size:14px;display:flex;align-items:center;gap:5px}
.footer-copy a{color:var(--link);border-left:2px solid var(--link);border-right:2px solid var(--link);padding:2px 6px}
</style>
</head>
<body>

<header class="hero" role="img" aria-label="Dusk photograph of a power plant chimney and industrial building">
  <div class="brand"><span class="brand-dot"></span>Corvana Power Holdings</div>
  <nav class="main-nav">
    <a>ABOUT US</a><a class="active">STRATEGY</a><a>PORTFOLIO</a><a>CONTACT</a>
  </nav>
  <h1 class="hero-title" style="font-weight:400">ILLUMINATING <span>THE FUTURE</span></h1>
  <p class="hero-sub">Investing in clean energy to generate sustainable<br>returns for our investors and planet</p>
</header>

<section class="stats">
  <div class="stat" style="left:177px"><div class="stat-num">10</div><div class="stat-label">Years of Operation</div></div>
  <div class="stat-div" style="left:371px"></div>
  <div class="stat" style="left:393px"><div class="stat-num">6</div><div class="stat-label">Countries of Investments</div></div>
  <div class="stat-div" style="left:589px"></div>
  <div class="stat" style="left:610px"><div class="stat-num">600</div><div class="stat-label">MW under Management</div></div>
  <div class="stat-div" style="left:807px"></div>
  <div class="stat" style="left:828px"><div class="stat-num">€500,000,000</div><div class="stat-label">Assets under Management</div></div>
</section>

<section class="about">
  <div class="eyebrow">EXPERTISE. RESOURCEFULNESS. INTEGRITY</div>
  <h2 class="panel-title" style="font-weight:400">ABOUT<br><span>US</span></h2>
  <p class="panel-text">Funding clean energy projects that maximise value to our investors and contribute to a more sustainable world</p>
  <a class="more-link"><u>More</u>
    <svg width="18" height="8" viewBox="0 0 18 8"><path d="M0 4h16M12 1l4 3-4 3" fill="none" stroke="currentColor" stroke-width="1.2"/></svg></a>
  <div class="accent-circle"></div>
  <div class="turbine-photo" role="img" aria-label="Photograph of a wind turbine above green farmland"></div>
</section>

<section class="team">
  <div class="eyebrow">HANDS-ON INVESTMENT MANAGEMENT</div>
  <h2 class="panel-title" style="font-weight:400">OUR<br>TEAM</h2>
  <p class="panel-text">Utilising our multi-disciplinary knowledge, sector expertise, extensive experience and collab-orative spirit</p>
  <a class="more-link"><u>More</u>
    <svg width="18" height="8" viewBox="0 0 18 8"><path d="M0 4h16M12 1l4 3-4 3" fill="none" stroke="currentColor" stroke-width="1.2"/></svg></a>
</section>

<section class="approach">
  <div class="approach-kicker">OUR APPROACH</div>
  <h2 class="approach-title" style="font-weight:400">PROVEN INVESTMENT STRATEGY</h2>
  <p class="approach-text">Achieving consistently high annualized returns and capital gains by leveraging our energy sector experience, broad geographic footprint, dedicated local networks, value creation and implementation of platform structures</p>
  <a class="btn-more">More
    <svg width="18" height="8" viewBox="0 0 18 8"><path d="M0 4h16M12 1l4 3-4 3" fill="none" stroke="currentColor" stroke-width="1.2"/></svg></a>
</section>

<p class="portfolio-intro">Corvana’ energy funds provide a diversified portfolio of assets - in operation and under construction,<br>in multiple markets - that drive high investment returns and a balanced risk profile</p>
<p class="portfolio-note">Map (focused on <a><u>UK, Italy, Spain, Israel, Poland</u></a> and<br>the <a><u>Netherlands</u></a>) with links to individual portfolio items</p>

<div class="map" role="img" aria-label="Grey polygon world map with highlighted portfolio countries in Europe and Israel">
  <svg class="map-lines" width="833" height="541" viewBox="0 0 833 541">
    <g stroke="#000" stroke-width="1.5">
      <line x1="389" y1="98" x2="389" y2="170"/>
      <line x1="436" y1="155" x2="420" y2="172"/>
      <line x1="493" y1="200" x2="475" y2="195"/>
      <line x1="375" y1="245" x2="355" y2="249"/>
      <line x1="448" y1="265" x2="440" y2="276"/>
      <line x1="522" y1="272" x2="500" y2="267"/>
    </g>
  </svg>
  <span class="map-tag" style="left:367px;top:88px">UK</span>
  <span class="map-tag" style="left:402px;top:148px">Netherlands</span>
  <span class="map-tag" style="left:498px;top:197px">Poland</span>
  <span class="map-tag" style="left:306px;top:241px">Spain</span>
  <span class="map-tag" style="left:412px;top:262px">Italy</span>
  <span class="map-tag" style="left:522px;top:264px">Israel</span>
</div>

<footer class="site-footer">
  <div class="footer-brand"><span class="footer-dot"></span>Corvana Power Holdings</div>
  <p class="footer-address">Corvana Power Holdings, Lavena Building, Kfar Orin, Ramat Eshel 47920 Israel</p>
  <div class="footer-contacts">
    <span>info@corvanafund.com</span>
    <span><b>Israel:</b> +972-3-555-0142</span>
    <span><b>Europe:</b> +44 (0) 20 5550 1190</span>
  </div>
  <a class="footer-credit"><u>Brightweave</u></a>
  <div class="footer-copy">© 2020 <a><u>Corvana Power Holdings</u></a></div>
</footer>

</body>
</html>
```